GLP letterhead

We need a letterhead design for our new company based in Los Angeles called "Gold Ladder Pictures". We develop film and television projects. We work with investors, financiers, film production companies, film distribution and sales companies as well as studios. We would like to incorporate our logo (see attached) but make the letterhead simple and elegant. We need to include: logo, company address, phone number and company website.
Updates

Hello designers, Thanks for your submissions. For our letterhead, we are looking for something more simple and elegant. No heavy bars or lines. Make it feel light and clean. Not a lot of ink on the page. Use the logo and contact info but think "clean", "streamlined" and mostly white paper. Looking forward to seeing more... thanks! Gold Ladder Pictures team

Target Market(s)

Studio executives, talent agents and agencies, financiers, investors.

Industry/Entity Type

It Company

Requirements
Must have
• Gold Ladder Pictures logo (see attached). Logo may be cropped and altered appropriately for elegant letterhead design.
• Please include:
• COMPANY ADDRESS:
• TQV Media Campus
• 2750 Halvering Avenue
• Norwick Center, 4th Floor
• Farrowdale Cove, CA 90999
• COMPANY WEBSITE:
• www.goldladderpicturesgroup.example
• COMPANY PHONE NUMBER:
• 555-014-2236

```html
<!DOCTYPE html>
<html lang="en">
<head>
<meta charset="utf-8">
<title>Gold Ladder Pictures — Letterhead</title>
<link rel="stylesheet" href="https://fonts.googleapis.com/css2?family=Crimson+Pro:wght@400;700&family=Montserrat:wght@600&display=swap">
<style>
  :root {
    --backdrop: #dedbd7;
    --paper: #ffffff;
    --ink: #1f1f1f;
    --ink-soft: #4a4a4a;
    --rule: #cfcfcf;
    --accent: #2a9ad0;
  }
  * { margin: 0; padding: 0; box-sizing: border-box; }
  html, body {
    width: 955px;
    height: 1200px;
    overflow: hidden;
    background: var(--backdrop);
  }
  .letterhead {
    position: absolute;
    left: 43px;
    top: 45px;
    width: 862px;
    height: 1115px;
    background: var(--paper);
  }
  .masthead {
    position: absolute;
    left: 0;
    top: 0;
    width: 100%;
    height: 147px;
    border-bottom: 1px solid var(--rule);
  }
  .brand {
    position: absolute;
    left: 20px;
    top: 20px;
    width: 196px;
    text-align: center;
  }
  .brand-mark {
    display: block;
    margin: 0 auto 8px;
  }
  .brand-name {
    font-family: "Crimson Pro", serif;
    font-size: 21px;
    color: var(--ink);
    letter-spacing: 0.4px;
    line-height: 1;
    white-space: nowrap;
  }
  .brand-tagline {
    margin-top: 10px;
    font-family: "Montserrat", sans-serif;
    font-weight: 600;
    font-size: 6.5px;
    letter-spacing: 1.9px;
    color: var(--ink-soft);
    white-space: nowrap;
  }
  .contact {
    position: absolute;
    left: 559px;
    top: 55px;
    padding-left: 16px;
    border-left: 1px solid var(--rule);
    font-family: "Crimson Pro", serif;
    font-variant-numeric: lining-nums;
    color: var(--ink);
  }
  .contact-row {
    display: flex;
    align-items: flex-start;
    gap: 8px;
  }
  .contact-row + .contact-row { margin-top: 10px; }
  .contact-icon { flex: none; margin-top: 1px; }
  .address {
    font-size: 15px;
    line-height: 16px;
    font-style: normal;
    white-space: nowrap;
  }
  .phone {
    font-weight: 700;
    font-size: 15px;
    letter-spacing: 0.6px;
    line-height: 16px;
  }
  .website {
    position: absolute;
    left: 0;
    bottom: 10px;
    width: 100%;
    text-align: center;
    font-family: "Crimson Pro", serif;
    font-weight: 700;
    font-size: 15px;
    letter-spacing: 1.4px;
    color: var(--ink);
  }
</style>
</head>
<body>
  <main class="letterhead">
    <header class="masthead">
      <div class="brand">
        <svg class="brand-mark" width="60" height="60" viewBox="0 0 60 60" aria-hidden="true">
          <circle cx="30" cy="30" r="28" fill="var(--accent)"/>
        </svg>
        <div class="brand-name">Gold Ladder Pictures</div>
        <div class="brand-tagline">A MEDIA ENTERTAINMENT COMPANY</div>
      </div>

      <div class="contact">
        <div class="contact-row">
          <svg class="contact-icon" width="14" height="14" viewBox="0 0 14 14" aria-hidden="true">
            <circle cx="7" cy="7" r="7" fill="var(--ink)"/>
            <path d="M3.3 7.2 L7 3.8 L10.7 7.2 M4.6 6.4 V10.3 H9.4 V6.4" fill="none" stroke="var(--paper)" stroke-width="1.3"/>
          </svg>
          <address class="address">
            TQV Media Campus<br>
            2750 Halvering Avenue Norwick Center<br>
            4th Floor Farrowdale Cove, CA 90999
          </address>
        </div>
        <div class="contact-row">
          <svg class="contact-icon" width="14" height="14" viewBox="0 0 14 14" aria-hidden="true">
            <circle cx="7" cy="7" r="7" fill="var(--ink)"/>
            <path d="M5 3.6 C4 4.4 3.9 6.6 5.3 8.6 C6.7 10.6 8.3 11 9.3 10.4 L8.4 8.8 L7.4 9.2 C6.6 8.6 6 7.6 5.8 6.6 L6.7 6 L6.3 4.2 Z" fill="var(--paper)"/>
          </svg>
          <span class="phone">555-014-2236</span>
        </div>
      </div>
    </header>

    <footer class="website">www.goldladderpicturesgroup.example</footer>
  </main>
</body>
</html>
```